Local Chiropractoc needs Modern Website

This website needs to have an upscale look with a very modern feel.

This is for a home page psd layout and an interior page psd file so 2 files total

Below is the information and websites to reference

Add Logo that is attached.

Build a color scheme similar to this website image titled "chiro-1" using the golds, whites, blacks and browns from the color of the logo

I want to see a light background so it makes the images and logo stick out

Must Include these pages in a horizontal menu bar in this order:
Home, Why Brightmoor?, How Chiropractic Helps, Ask the Doctor, Work Place Wellness, Request an Appointment, Blog, Contact Us

Please add the following social media logos to the top and footer of the website: Chatterly, Vexora+, Streamlo

Build a "classy looking" Make An Appointment Button into the header with the contact info below

Phone Number:
555-014-2739

Address:
4128 North Tamsin Blvd, Suite #7
Harrowgate, GA 30917

This website needs 4 rotating banners. Please reference a layout similar to this for the banners: http://quarrelstonechiro.example/. However design it nicer than this website

Below are the description for each banner

Rotating Banner #1
Use Image: Patients are Saying
Add a line of text: "What our Patients are Saying"

Rotating Banner #2
Use Image: Becoming a Patient
Add a line of text: "Interested in Becoming a Patient"

Rotating Banner #3
Use Image: Dinner with Doctor
Add a line of text: "Win A free Dinner with Dr. Halloway"

Rotating Banner #4
Use Image: Chatterly
Add a line of text: Follow us on Chatterly
Bullet point these 4 lines underneath the "Follow us on Chatterly" text:
- Cutting Edge Health News
- Healthy Recipes
- Newest Health Products
- Clinic Events

I'd like to see a free consultation box similar to the "chiro-1" image. Fields to include are: First Name, Last Name, Phone Number, Comments

For the body, please fill it with latin text. Please design a professional 2 column layout similar to the www.quarrelstonechiro.example website. (DO NOT COPY THIS WEBSITE, USE IT AS REFERENCE)

In the left column include in this order:
Video
Rate us on Vexora Button, Find us on Chatterly Button
Welcome Letter

In the right column include this:

Office Hours
Monday: 8:00-11:00, 2:00-5:00
Tuesday: 8:30-11:00, 2:00-5:30
Wednesday: 8:00-11:00, 2:00-5:00
Thursday: 10:00-12:00, 2:30-5:00
Friday: 8:00-10:00, 1:00-5:00
Saturday: Closed
Sunday: Closed

Patient Testimonials
Fill with a latin text testimonial. This spot will rotate different testimonials

For the footer please design something similar to the layout of this: http://www.verdantpathspinecare.example/

Also include in the Footer: Powered by Pixelmere Web Group

```html
<!DOCTYPE html>
<html lang="en">
<head>
<meta charset="utf-8">
<title>Brightmoor Chiropractic</title>
<link href="https://fonts.googleapis.com/css2?family=Open+Sans:wght@400;600;700;800&display=swap" rel="stylesheet">
<style>
:root{
  --gold:#a8874a;
  --gold-light:#c9a968;
  --gold-dark:#7a5f2c;
  --black:#111;
  --text:#333;
  --muted:#999;
  --rule:#d8c9a8;
  --footer-gray:#e3e3e3;
}
*{margin:0;padding:0;box-sizing:border-box}
html,body{width:761px;height:1200px;overflow:hidden;background:#fff}
body{font-family:"Open Sans",Arial,sans-serif;color:var(--text);position:relative}
.abs{position:absolute}
/* header */
.logo{left:101px;top:32px;display:flex;align-items:center;gap:5px}
.logo-mark{width:9px;height:34px;background:var(--black)}
.logo-name{font-weight:800;font-size:13px;line-height:14px;color:var(--black);letter-spacing:-.2px;display:block}
.logo-sub{font-weight:700;font-size:7px;color:var(--gold);letter-spacing:.6px;display:block;margin-top:2px}
.phone{left:328px;top:42px;display:flex;align-items:center;gap:8px;font-size:7px;color:#222}
.divider{left:405px;top:34px;width:1px;height:30px;background:#ccc}
.address{left:420px;top:38px;display:flex;gap:9px;font-size:5.5px;line-height:10px;color:#888}
.address b{color:#222;font-weight:600}
.btn-appt{left:563px;top:38px;width:97px;height:24px;border-radius:3px;background:linear-gradient(#c8a866,#8a6a30);color:#fff;font-size:6px;font-weight:700;text-align:center;line-height:24px;box-shadow:0 2px 3px rgba(0,0,0,.35)}
/* nav */
.nav{left:0;top:73px;width:761px;height:39px;background:linear-gradient(#3a3a3a,#0c0c0c);display:flex;align-items:center}
.nav a{color:#fff;text-decoration:none;font-size:6.5px;font-weight:700;padding:0 13px;height:39px;line-height:39px;border-right:1px solid #4a4a4a;white-space:nowrap;position:relative}
.nav a.current::after{content:"";position:absolute;left:50%;bottom:-1px;margin-left:-6px;border:6px solid transparent;border-bottom-color:var(--gold-light)}
.social{display:flex;gap:6px}
.social span{width:20px;height:20px;background:#5a5a5a;color:#ddd;font-size:6px;font-weight:700;display:flex;align-items:center;justify-content:center}
.nav .social{margin-left:auto;margin-right:15px}
/* hero */
.hero{left:0;top:112px;width:761px;height:290px;background:radial-gradient(ellipse at 40% 45%,#f0d2bd 0%,#e5b99a 35%,#c9b36c 65%,#93a55a 100%);overflow:hidden}
.hero-band{left:0;top:0}
.hero-card{left:483px;top:38px;width:177px;height:152px;background:rgba(30,28,24,.82);border:1px solid #777;color:#eee;padding:12px 10px}
.hero-card h3{font-weight:400;font-size:10px;border-bottom:1px solid #777;padding-bottom:6px;margin-bottom:8px}
.hero-card p{font-size:7.5px;line-height:13px}
.hero-card .more{position:absolute;left:0;right:0;bottom:0;height:42px;background:rgba(0,0,0,.35);text-align:center;line-height:42px;font-size:7px;font-weight:700;color:#bbb}
.hero-card .more::before{content:"";position:absolute;left:50%;top:-8px;margin-left:-8px;border:8px solid transparent;border-top:0;border-bottom-color:rgba(0,0,0,.35)}
.hero-line{left:101px;top:259px;color:#fff;font-size:7px;font-weight:700;letter-spacing:.1px}
.hero-contact{left:584px;top:253px;width:75px;height:25px;border:1px solid #aaa;color:#fff;font-size:5.5px;display:flex;align-items:center;justify-content:space-around}
/* sections */
.section-title{font-size:8px;font-weight:700;color:#111}
.section-sub{font-size:5px;color:#aaa;margin-top:1px}
.rule{height:1px;background:var(--rule)}
.video{left:103px;top:477px;width:364px;height:190px;border:1px solid #ccc;background:linear-gradient(180deg,#f3dcc8 0%,#e8c4a6 45%,#d8b36a 70%,#b79840 100%)}
.video-bar{position:absolute;left:0;right:0;bottom:0;height:16px;background:#1c1c1c;display:flex;align-items:center;padding:0 8px;gap:8px;color:#ccc;font-size:6px}
.video-track{flex:1;height:3px;background:#555;position:relative}
.video-track i{position:absolute;left:22%;top:-3px;width:9px;height:9px;border-radius:50%;background:#ddd}
.rate-btn{width:160px;height:63px;border-radius:5px;background:linear-gradient(#c4a25f,#7d6130);box-shadow:0 2px 3px rgba(0,0,0,.3);color:#fff;text-align:center}
.rate-btn small{display:block;font-size:8px;font-weight:700;color:#3b2b10;padding-top:12px}
.rate-btn strong{display:block;font-size:21px;font-weight:700;line-height:28px}
.copy{font-size:5px;line-height:9.5px;color:#555}
.card{width:177px;height:128px;border:1px solid #ddd;border-radius:4px;overflow:hidden;background:#fff}
.card .img{height:62px}
.card h4{font-size:7px;font-weight:700;color:#111;margin:6px 4px 4px}
.card p{font-size:5.5px;line-height:9px;color:#555;margin:0 4px}
.card .more{position:absolute;right:8px;bottom:8px;font-size:5px;color:var(--gold)}
/* sidebar */
.panel{border:1px solid #ccc;background:#fff}
.panel-head{background:var(--black);color:#fff;font-size:8px;font-weight:700;text-align:center;height:27px;line-height:27px}
.hours{font-size:5.5px;padding:8px 9px 0}
.hours div{display:flex;justify-content:space-between;height:13.5px}
.hours .closed{color:var(--gold)}
.consult-head{height:62px;position:relative}
.consult-head svg{position:absolute;left:-1px;top:-1px}
.consult-head p{position:absolute;left:0;right:0;text-align:center;font-size:7px;color:var(--gold-light)}
.form{padding:0 9px}
.form h5{font-size:7.5px;font-weight:700;color:#111;margin:12px 0 10px}
.form label{display:block;font-size:5.5px;color:#222;margin-bottom:3px}
.form .field{height:14px;border:1px solid #bbb;margin-bottom:10px}
.form .area{height:48px;margin-bottom:9px}
.submit{width:60px;height:20px;border-radius:3px;background:linear-gradient(#c4a25f,#7d6130);color:#fff;font-size:6px;font-weight:700;line-height:20px;text-align:center;letter-spacing:1px}
.quote{font-size:5px;line-height:9px;color:#444;padding:0 22px;text-align:center}
.arrow-btn{width:20px;height:17px;background:linear-gradient(#c4a25f,#7d6130);color:#fff;font-size:8px;text-align:center;line-height:17px}
/* footer */
.footer-top{left:0;top:1126px;width:761px;height:36px;background:var(--footer-gray)}
.footer-bottom{left:0;top:1162px;width:761px;height:38px;background:var(--gold)}
.footer-meta{left:101px;top:1172px;font-size:5px;line-height:9px;color:#3a2c12}
.footer-nav{left:258px;top:1184px;display:flex;gap:10px;font-size:5px;color:#fff;font-weight:600}
.to-top{left:641px;top:1174px;width:18px;height:18px;border:1px solid #d9c494;color:#fff;font-size:7px;text-align:center;line-height:16px}
</style>
</head>
<body>

<header>
  <div class="abs logo">
    <span class="logo-mark"></span>
    <div><span class="logo-name">BRIGHTMOOR</span><span class="logo-sub">CHIROPRACTIC</span></div>
  </div>
  <div class="abs phone">
    <svg width="12" height="12" viewBox="0 0 24 24"><path fill="#222" d="M6.6 10.8a15.1 15.1 0 0 0 6.6 6.6l2.2-2.2a1 1 0 0 1 1-.25 11.4 11.4 0 0 0 3.6.57 1 1 0 0 1 1 1V20a1 1 0 0 1-1 1A17 17 0 0 1 3 4a1 1 0 0 1 1-1h3.5a1 1 0 0 1 1 1c0 1.25.2 2.45.57 3.57a1 1 0 0 1-.25 1z"/></svg>
    555-014-2739
  </div>
  <div class="abs divider"></div>
  <div class="abs address">
    <svg width="16" height="15" viewBox="0 0 24 22"><path fill="#222" d="M12 1 1 11h3v10h6v-6h4v6h6V11h3z"/></svg>
    <div>4128 North Tamsin Blvd, Suite #7<br><b>HARROWGATE, GA 30917</b></div>
  </div>
  <div class="abs btn-appt">MAKE AN APPOINTMENT</div>
</header>

<nav class="abs nav">
  <a>HOME</a>
  <a class="current">WHY BRIGHTMOOR?</a>
  <a>HOW CHIROPRACTIC HELPS</a>
  <a>ASK THE DOCTOR</a>
  <a>WORK PLACE WELLNESS</a>
  <a>REQUEST AN APPOINTMENT</a>
  <a>BLOG</a>
  <a>CONTACT US</a>
  <div class="social"><span>C</span><span>V+</span><span>S</span></div>
</nav>

<section class="abs hero" role="img" aria-label="Banner photo of a smiling baby flexing both arms">
  <svg class="abs hero-band" width="761" height="290" viewBox="0 0 761 290">
    <path d="M0 240 Q380 190 761 240 L761 290 L0 290Z" fill="rgba(40,36,30,.85)"/>
  </svg>
  <div class="abs hero-card">
    <h3>Quam eleifend metus commodo</h3>
    <p>luctus at sit amet urna. Quisque non augue as massa non, elementum sem. Suspendiss eu lorem ultricies dapibus.</p>
    <div class="more">Learn more &#9758;</div>
  </div>
  <div class="abs hero-line">QUAM ELEIFEND METUS COMMODO &nbsp;UCTUS AT SIT AMET URNA &nbsp;QUISQUE NON AUGUE TINCIDUNT EG</div>
  <div class="abs hero-contact"><span>Contact Us</span>
    <svg width="12" height="9" viewBox="0 0 12 9"><rect x=".5" y=".5" width="11" height="8" fill="none" stroke="#ccc"/><path d="M.5.5 6 5l5.5-4.5" fill="none" stroke="#ccc"/></svg>
  </div>
</section>

<main>
  <div class="abs" style="left:101px;top:438px;width:366px">
    <div class="section-title">OUR VIDEOS</div>
    <div class="section-sub">Lorem ipsum dolor sit amet, consect</div>
    <div class="rule" style="margin-top:9px"></div>
  </div>
  <div class="abs video" role="img" aria-label="Video still of a baby beside juice and fresh fruit">
    <div class="video-bar"><span>&#9654;</span><div class="video-track"><i></i></div><span>1:30 - 4:23</span><span>&#9632;</span></div>
  </div>

  <div class="abs rate-btn" style="left:101px;top:689px"><small>RATE US ON:</small><strong>Vexora</strong></div>
  <div class="abs rate-btn" style="left:306px;top:689px"><small>FIND US ON:</small><strong>Chatterly</strong></div>

  <div class="abs" style="left:101px;top:775px;width:366px">
    <div class="section-title">WELCOME LETTER</div>
    <div class="section-sub">Lorem ipsum dolor sit amet, consect</div>
    <div class="rule" style="margin-top:5px;margin-bottom:6px"></div>
    <p class="copy">Sed ut perspiciatis unde omnis iste natus error sit voluptatem accusantium doloremque laudantium, totam rem aperiam, eaque ipsa quae ab illo inventore veritatis et quasi architecto beatae vitae dicta sunt explicabo nemo enim ipsam.</p>
    <p class="copy" style="margin-top:5px">Neque porro quisquam est, qui dolorem ipsum quia dolor sit amet, consectetur, adipisci velit, sed quia non numquam eius modi tempora incidunt ut labore et dolore magnam aliquam quaerat voluptatem. Ut enim ad minima veniam, quis nostrum exercitationem ullam corporis suscipit laboriosam, nisi ut aliquid ex ea commodi consequatur. Quis autem vel eum iure reprehenderit qui in ea voluptate velit esse quam nihil molestiae consequatur, vel illum qui dolorem eum fugiat quo voluptas nulla pariatur.</p>
    <div class="copy" style="text-align:right;color:var(--muted)">Read More &#9758;</div>
  </div>

  <div class="abs" style="left:101px;top:898px;width:366px">
    <div class="section-title">WELCOME LETTER</div>
    <div class="section-sub">Lorem ipsum dolor sit amet, consect</div>
    <div class="rule" style="margin-top:9px"></div>
  </div>
  <div class="abs card" style="left:101px;top:939px">
    <div class="img" role="img" aria-label="Photo of carrots, oranges and apples" style="background:linear-gradient(90deg,#f3c06a,#e9983a 45%,#d8c27a)"></div>
    <h4>LOREM IPSUM DOLOR</h4>
    <p>Neque porro quisquam est, qui dolorem ipsum quia dolor sit amet Neque porro quisquam est, qui dolorem ipsum qu ia dolor sit amet</p>
    <span class="more">Read More &#9758;</span>
  </div>
  <div class="abs card" style="left:290px;top:939px">
    <div class="img" role="img" aria-label="Photo of a smiling family" style="background:linear-gradient(90deg,#c79a74,#e6c2a1 50%,#a88660)"></div>
    <h4>LOREM IPSUM DOLOR</h4>
    <p>Neque porro quisquam est, qui dolorem ipsum quia dolor sit amet Neque porro quisquam est, qui dolorem ipsum qu ia dolor sit amet</p>
    <span class="more">Read More &#9758;</span>
  </div>
</main>

<aside>
  <div class="abs panel" style="left:483px;top:439px;width:176px;height:141px">
    <div class="panel-head">OFFICE HOURS</div>
    <div class="hours">
      <div><span>Monday:</span><span>8:00-11:00, 2:00-5:00</span></div>
      <div><span>Tuesday:</span><span>8:30-11:00, 2:00-5:30</span></div>
      <div><span>Wednesday:</span><span>8:00-11:00, 2:00-5:00</span></div>
      <div><span>Thursday:</span><span>10:00-12:00, 2:30-5:00</span></div>
      <div><span>Friday:</span><span>8:00-10:00, 1:00-5:00</span></div>
      <div class="closed"><span>Saturday:</span><span>Closed</span></div>
      <div class="closed"><span>Sunday:</span><span>Closed</span></div>
    </div>
  </div>

  <div class="abs panel" style="left:483px;top:593px;width:176px;height:292px">
    <div class="consult-head">
      <svg width="176" height="64" viewBox="0 0 176 64"><path d="M0 0H176V46L88 64 0 46Z" fill="#111"/></svg>
      <p style="top:10px">CONTACT US NOW &amp; GET YOUR</p>
      <p style="top:23px;color:#fff;font-weight:700">FREE CONSULTATION</p>
      <p style="top:37px;font-weight:700">&mdash;&mdash; TODAY ! &mdash;&mdash;</p>
    </div>
    <div class="form">
      <h5>WELLNESS BEGINS HERE</h5>
      <label>First Name</label><div class="field"></div>
      <label>Last Name</label><div class="field"></div>
      <label>Phone Number</label><div class="field"></div>
      <label>Comments</label><div class="field area"></div>
      <div class="submit">SUBMIT &#9758;</div>
    </div>
  </div>

  <div class="abs panel" style="left:483px;top:900px;width:176px;height:167px;overflow:hidden">
    <div class="panel-head">PATIENT TESTEMONIALS</div>
    <div style="position:absolute;left:12px;top:44px;font-size:14px;color:#111">&ldquo;</div>
    <div style="position:absolute;right:10px;top:56px;font-size:14px;color:#111">&rdquo;</div>
    <p class="quote" style="margin-top:32px">veniam, quis nostrum exercitationem ullam Ut enim ad veniam, qu veniam, quis nostrum exercitationem ullam Ut enim</p>
    <div style="display:flex;justify-content:space-between;align-items:center;padding:0 19px;margin-top:12px">
      <span class="arrow-btn">&#8249;</span>
      <em style="font-size:8px;color:#111">-Marisol Venn-</em>
      <span class="arrow-btn">&#8250;</span>
    </div>
    <svg style="position:absolute;left:0;bottom:0" width="176" height="48" viewBox="0 0 176 48"><path d="M0 6H80L88 0 96 6H176V48H0Z" fill="#111"/><path d="M0 6H80L88 0 96 6H176" fill="none" stroke="#c9a968" stroke-width="2"/></svg>
    <div style="position:absolute;left:0;right:0;bottom:14px;text-align:center;color:#bbb;font-size:7.5px;font-weight:700">Read more &#9758;</div>
  </div>
</aside>

<footer>
  <div class="abs footer-top"></div>
  <div class="abs logo" style="top:1130px">
    <span class="logo-mark" style="height:28px"></span>
    <div><span class="logo-name" style="font-size:11px;line-height:12px">BRIGHTMOOR</span><span class="logo-sub" style="font-size:6px">CHIROPRACTIC</span></div>
  </div>
  <div class="abs social" style="left:590px;top:1136px"><span>C</span><span>V+</span><span>S</span></div>
  <div class="abs footer-bottom"></div>
  <div class="abs footer-meta">4128 North Tamsin Blvd, Suite #7 &nbsp;HARROWGATE, GA 30917<br><b>Powered by Pixelmere Web Group</b> &copy; Copyright 2015</div>
  <div class="abs footer-nav"><span>Home</span><span>Why Brightmoor?</span><span>How Chiropractic Helps</span><span>Ask the Doctor</span><span>Work Place Wellness</span><span>Request an Appointment</span><span>Blog</span><span>Contact Us</span></div>
  <div class="abs to-top">&#8963;</div>
</footer>

</body>
</html>
```